fieldscoutingpath.com - Social Media Branding

fieldscoutingpath.com --> Social Media Re-Branding & Graphics
Facebook: @fldscoutpath - Instagram: @fieldscoutingpath - Twitter: @fldscoutpath

Looking to find a good designer to help with my fieldscoutingpath.com social media sites!
- facebook banner
- twitter banner
- instagram template (square and banner size)
- Quote or Information Template
- Committed Template (uniformed) - see the ones I made (& i am no professional) at fieldscoutingpath.com/committed - needs to have fieldscoutingpath.com logo, room for: the committed school and the team the player plays on.

Also willing to pay extra for a graphic that is the "complete package" that detail all of the steps of the recruiting process detailed in fieldscoutingpath.com

Font styles to use
Sans Serif

Colors
ec1f27
fbee3e

```html
<!DOCTYPE html>
<html lang="en">
<head>
<meta charset="utf-8">
<title>fieldscoutingpath.com – Social Media Banners</title>
<link href="https://fonts.googleapis.com/css2?family=Jost:wght@500;600;700;800&display=swap" rel="stylesheet">
<style>
  :root{
    --board:#1b1b1b;
    --red:#c21f32;
    --brand-red:#ec1f27;
    --yellow:#f0f05a;
    --brand-yellow:#fbee3e;
    --ink:#0d0d0d;
    --white:#ffffff;
    --grey:#5a5a5a;
  }
  *{box-sizing:border-box;margin:0;padding:0}
  html,body{width:755px;height:1200px;overflow:hidden;background:var(--board)}
  body{position:relative;font-family:"Jost",sans-serif}
  .banner{position:absolute;overflow:hidden}
  .photo{position:absolute;inset:0}
  .brand{position:absolute;display:flex;align-items:center;gap:6px;font-weight:600;white-space:nowrap}
  .brand-dot{border-radius:50%;flex:none}
  .kicker,.headline{position:absolute;white-space:nowrap;text-transform:uppercase;line-height:1}
  .kicker{font-weight:600;letter-spacing:.3px}
  .headline{font-weight:800;letter-spacing:-.3px}
  .cta{position:absolute;display:flex;align-items:center;justify-content:center;border-radius:999px;font-weight:700;text-transform:uppercase;letter-spacing:.4px}

  /* Facebook cover */
  .cover-light{left:26px;top:23px;width:705px;height:268px;background:var(--white)}
  .cover-light .photo{left:300px;background:linear-gradient(180deg,#8fc3e4 0%,#5f8f5a 40%,#c8a88a 62%,#a98b73 100%)}
  .cover-light .fade{position:absolute;inset:0;left:300px;background:linear-gradient(90deg,#fff 0%,rgba(255,255,255,.7) 25%,rgba(255,255,255,0) 55%)}
  .cover-light .brand{left:46px;top:54px;font-size:17px;color:var(--grey)}
  .cover-light .brand-dot{width:26px;height:26px;background:var(--brand-yellow)}
  .cover-light .kicker{left:45px;top:101px;font-size:21px;color:var(--red)}
  .cover-light .headline{left:44px;top:128px;font-size:45px;color:var(--ink)}
  .cover-light .cta{left:43px;top:193px;width:209px;height:42px;background:var(--yellow);color:var(--white);font-size:21px}

  /* Warm gradient banners */
  .warm .photo{background:
    radial-gradient(circle at 83% 78%,rgba(240,220,80,.9) 0 11%,rgba(0,0,0,0) 12%),
    linear-gradient(100deg,#c8384a 0%,#d9604a 40%,#dfa04a 70%,#e5c23e 100%)}
  .warm .ground{position:absolute;left:0;right:0;bottom:0;height:40%;background:linear-gradient(180deg,rgba(200,70,40,0),rgba(210,90,40,.55))}
  .warm .brand,.warm .kicker,.warm .headline{color:var(--white)}
  .warm .brand-dot{background:var(--white)}
  .warm .cta-outline{border:1.5px solid var(--white);color:var(--white)}

  .cover-warm{left:27px;top:313px;width:705px;height:268px}
  .cover-warm .brand{left:0;right:0;justify-content:center;top:50px;font-size:16px}
  .cover-warm .brand-dot{width:24px;height:24px}
  .cover-warm .kicker{left:163px;top:100px;font-size:23px}
  .cover-warm .headline{left:162px;top:127px;font-size:50px}
  .cover-warm .cta{left:270px;top:190px;width:158px;height:31px;font-size:17px}

  .post-warm{left:27px;top:602px;width:344px;height:273px}
  .post-warm .photo{background:
    radial-gradient(circle at 82% 64%,rgba(240,230,90,.9) 0 13%,rgba(0,0,0,0) 14%),
    linear-gradient(110deg,#c83a4e 0%,#d8604a 45%,#e0a54a 80%,#e8c64a 100%)}
  .post-warm .brand{left:0;right:0;justify-content:center;top:58px;font-size:12px}
  .post-warm .brand-dot{width:18px;height:18px}
  .post-warm .kicker{left:41px;top:108px;font-size:17.5px}
  .post-warm .headline{left:40px;top:134px;font-size:36px}
  .post-warm .cta{left:107px;top:189px;width:126px;height:25px;font-size:13px}

  /* Square light post */
  .post-light{left:387px;top:602px;width:344px;height:344px;background:var(--white)}
  .post-light .photo{bottom:auto;height:230px;background:linear-gradient(180deg,#6fb3e0 0%,#4f8a4e 40%,#b9a690 75%,#ffffff 100%)}
  .post-light .fade{position:absolute;left:0;right:0;top:120px;height:115px;background:linear-gradient(180deg,rgba(255,255,255,0),#fff)}
  .post-light .brand{left:0;right:0;justify-content:center;top:193px;font-size:12px;color:var(--ink)}
  .post-light .brand-dot{width:18px;height:18px;background:var(--brand-yellow)}
  .post-light .kicker{left:51px;top:235px;font-size:16px;color:var(--red)}
  .post-light .headline{left:50px;top:251px;font-size:33px;color:var(--ink)}
  .post-light .cta{left:111px;top:295px;width:128px;height:25px;background:var(--red);color:var(--white);font-size:12px;box-shadow:0 3px 6px rgba(0,0,0,.25)}

  /* Quote template */
  .quote-card{left:27px;top:888px;width:344px;height:283px}
  .quote-card .photo{background:
    radial-gradient(circle at 84% 50%,#e5ef5a 0 18%,rgba(0,0,0,0) 19%),
    linear-gradient(180deg,#d99aa4 0%,#b9864a 22%,#d07040 70%,#d8823f 100%)}
  .quote-band{position:absolute;left:0;right:0;top:69px;height:148px;background:linear-gradient(90deg,rgba(200,40,60,.92) 0%,rgba(205,55,55,.85) 65%,rgba(205,60,55,.2) 100%)}
  .quote-mark{position:absolute;left:94px;top:80px;width:24px;height:22px}
  .quote-text{position:absolute;left:22px;top:116px;width:210px;font-size:9.9px;line-height:14.4px;color:var(--white);font-weight:500}
  .quote-author{position:absolute;right:99px;top:192px;font-size:11px;font-weight:700;color:var(--white);letter-spacing:.3px}
  .quote-card .brand{left:0;right:0;justify-content:center;top:248px;font-size:11.5px}
  .quote-card .brand-dot{width:18px;height:18px}
</style>
</head>
<body>

<section class="banner cover-light">
  <div class="photo" role="img" aria-label="Softball batter swinging with catcher crouched behind plate on a sunny field"></div>
  <div class="fade"></div>
  <div class="brand"><span class="brand-dot"></span>fieldscoutingpath.com</div>
  <p class="kicker">Over 2 million dollars in</p>
  <h1 class="headline">Scholarships</h1>
  <a class="cta">Get started</a>
</section>

<section class="banner warm cover-warm">
  <div class="photo" role="img" aria-label="Yellow softball resting on infield dirt under a red-to-yellow tint"></div>
  <div class="ground"></div>
  <div class="brand"><span class="brand-dot"></span>fieldscoutingpath.com</div>
  <p class="kicker">Over 2 million dollars in</p>
  <h2 class="headline">Scholarships</h2>
  <a class="cta cta-outline">Get started</a>
</section>

<section class="banner warm post-warm">
  <div class="photo" role="img" aria-label="Yellow softball on infield dirt under a warm gradient tint"></div>
  <div class="ground"></div>
  <div class="brand"><span class="brand-dot"></span>fieldscoutingpath.com</div>
  <p class="kicker">Over 2 million dollars in</p>
  <h2 class="headline">Scholarships</h2>
  <a class="cta cta-outline">Get started</a>
</section>

<section class="banner post-light">
  <div class="photo" role="img" aria-label="Softball batter and catcher at home plate on a sunny field"></div>
  <div class="fade"></div>
  <div class="brand"><span class="brand-dot"></span>fieldscoutingpath.com</div>
  <p class="kicker">Over 2 million dollars in</p>
  <h2 class="headline">Scholarships</h2>
  <a class="cta">Get started</a>
</section>

<section class="banner warm quote-card">
  <div class="photo" role="img" aria-label="Close-up of a yellow softball on infield dirt"></div>
  <div class="quote-band"></div>
  <svg class="quote-mark" viewBox="0 0 24 22" aria-hidden="true">
    <path fill="#fff" d="M1 1h9v10c0 5-3 9-8 10l-1-3c3-1 4-3 4-6H1z M14 1h9v10c0 5-3 9-8 10l-1-3c3-1 4-3 4-6h-4z"/>
  </svg>
  <p class="quote-text">Lorem ipsum dolor sit amet, consectetur adipiscing elit, sed do eiusmod tempor incididunt ut labore et dolore magna aliqua. Quis ipsum suspendisse ultrices gravida. Risus commodo viverra maecenas</p>
  <p class="quote-author">JOHN SMITH</p>
  <div class="brand"><span class="brand-dot"></span>fieldscoutingpath.com</div>
</section>

</body>
</html>
```